I own a self service Laundromat. From time to time our machines break or take the customers money. I would like to design a post card that I can send the customer that had trouble with one of the machines along with the return of their money. Maybe on one side of the card say OOPS! with a picture of a clothes washer or clothes dryer. On the other side some text that says we are sorry for the trouble at your last visit. Please see attached return of money and we would love to have you back and satisfied. Thank you again for visiting The Suds Corner. I currently don't have a logo so be as creative as you like.

```html
<!DOCTYPE html>
<html lang="en">
<head>
<meta charset="utf-8">
<title>The Suds Corner – Apology Postcard</title>
<link href="https://fonts.googleapis.com/css2?family=Open+Sans:wght@400;600;700;800&display=swap" rel="stylesheet">
<style>
  :root {
    --page-bg: #eeeeee;
    --card-white: #ffffff;
    --sky-top: #c9e8f4;
    --sky-mid: #e6f5fb;
    --wave-blue: #7cc6e6;
    --wave-light: #b5e0f1;
    --green: #5db449;
    --green-dark: #3f8f32;
    --text-dark: #2a3a44;
    --steel: #a9b2b8;
    --steel-dark: #6f7a82;
    --wicker: #8a5a34;
    --burlap: #c9a978;
    --room-tone: #dfe7ea;
    --shirt: #f3f6f8;
  }
  * { margin: 0; padding: 0; box-sizing: border-box; }
  html, body { width: 853px; height: 1200px; overflow: hidden; }
  body {
    background: var(--page-bg);
    font-family: "Open Sans", Arial, sans-serif;
    position: relative;
  }
  .postcard {
    position: absolute;
    left: 185px;
    width: 597px;
    height: 478px;
    background: var(--card-white);
    overflow: hidden;
    box-shadow: 0 4px 14px rgba(0,0,0,0.18);
  }
  .postcard--front { top: 62px; }
  .postcard--back { top: 566px; height: 481px; }

  .front-sky {
    position: absolute; inset: 0;
    background: linear-gradient(180deg, var(--sky-top) 0%, var(--sky-mid) 55%, var(--card-white) 80%);
  }
  .wave { position: absolute; left: 0; width: 100%; }
  .wave--front-bottom { bottom: 0; height: 120px; }
  .wave--back-top { top: 0; height: 90px; }
  .wave--back-bottom { bottom: 0; height: 70px; }

  .art { position: absolute; }
  .art--washer {
    left: 28px; top: 8px; width: 250px; height: 330px;
    border-radius: 10px;
    background: linear-gradient(135deg, #d6dce0 0%, var(--steel) 55%, var(--steel-dark) 100%);
  }
  .art--basket {
    left: 10px; top: 255px; width: 175px; height: 140px;
    border-radius: 12px 12px 40px 40px;
    background: linear-gradient(180deg, #9fb7b9 0%, var(--wicker) 45%, #6b4224 100%);
  }
  .art--money-bag {
    left: 385px; top: 225px; width: 160px; height: 160px;
    border-radius: 45% 45% 20% 20%;
    background: linear-gradient(180deg, #8fae7d 0%, var(--burlap) 45%, #a88655 100%);
  }

  .speech-bubble {
    position: absolute;
    background: var(--green);
    color: var(--card-white);
    border-radius: 10px;
    text-align: center;
    box-shadow: 0 2px 4px rgba(0,0,0,0.2);
  }
  .speech-bubble::after {
    content: "";
    position: absolute;
    border-style: solid;
  }
  .speech-bubble--oops {
    left: 362px; top: 100px; width: 192px; height: 118px;
    padding-top: 8px;
  }
  .speech-bubble--oops::after {
    left: 22px; bottom: -22px;
    border-width: 22px 18px 0 0;
    border-color: var(--green) transparent transparent transparent;
  }
  .bubble-kicker {
    font-size: 13px; font-weight: 600; letter-spacing: 4px;
    color: #e5f6de;
  }
  .bubble-headline {
    font-size: 50px; font-weight: 800; line-height: 1.05; letter-spacing: 1px;
  }
  .bubble-brand { font-size: 15px; font-weight: 600; margin-top: 2px; }

  .back-room {
    position: absolute; left: 0; top: 40px; width: 100%; height: 390px;
    background: linear-gradient(180deg, #eef3f5 0%, var(--room-tone) 50%, #f4f7f8 100%);
    opacity: 0.7;
  }
  .back-veil {
    position: absolute; left: 0; top: 0; width: 360px; height: 100%;
    background: linear-gradient(90deg, rgba(255,255,255,0.85) 60%, rgba(255,255,255,0));
  }
  .art--customer {
    left: 360px; top: 40px; width: 230px; height: 370px;
    border-radius: 6px;
    background: linear-gradient(180deg, #d9cfc6 0%, var(--shirt) 40%, #d8a9a2 75%, #c9b9a3 100%);
  }
  .speech-bubble--sorry {
    left: 80px; top: 62px; width: 205px; height: 100px;
    padding-top: 12px;
  }
  .speech-bubble--sorry::after {
    left: 28px; bottom: -20px;
    border-width: 20px 0 0 18px;
    border-color: var(--green) transparent transparent transparent;
  }
  .sorry-title { font-size: 24px; font-weight: 700; line-height: 1.1; }
  .sorry-sub { font-size: 14px; font-weight: 600; line-height: 1.35; margin-top: 4px; }

  .apology-message {
    position: absolute; left: 60px; top: 212px; width: 260px;
    text-align: center; color: var(--text-dark);
  }
  .apology-body { font-size: 13px; font-weight: 600; line-height: 1.45; }
  .apology-thanks { font-size: 16px; font-weight: 700; line-height: 1.35; margin-top: 18px; }

  .store-address {
    position: absolute; left: 30px; bottom: 48px;
    font-size: 13px; font-weight: 700; color: var(--text-dark);
  }
</style>
</head>
<body>

  <section class="postcard postcard--front">
    <div class="front-sky"></div>
    <svg class="wave wave--front-bottom" viewBox="0 0 597 120" preserveAspectRatio="none">
      <path d="M0 55 C150 20 320 95 597 40 L597 120 L0 120 Z" fill="var(--wave-light)"/>
      <path d="M0 75 C170 45 330 110 597 62 L597 120 L0 120 Z" fill="var(--wave-blue)"/>
      <path d="M0 90 C180 65 340 120 597 82 L597 120 L0 120 Z" fill="var(--card-white)"/>
    </svg>
    <div class="art art--washer" role="img" aria-label="Front-loading stainless steel washing machine"></div>
    <div class="art art--basket" role="img" aria-label="Wicker basket of folded towels"></div>
    <div class="art art--money-bag" role="img" aria-label="Burlap sack filled with dollar bills"></div>
    <div class="speech-bubble speech-bubble--oops">
      <div class="bubble-kicker">WE GOOFED</div>
      <div class="bubble-headline">OOPS!</div>
      <div class="bubble-brand">The Suds Corner</div>
    </div>
  </section>

  <section class="postcard postcard--back">
    <div class="back-room" role="img" aria-label="Soft faded view of a bright laundromat with rows of washers"></div>
    <div class="back-veil"></div>
    <div class="art art--customer" role="img" aria-label="Smiling customer holding a laundry basket"></div>
    <svg class="wave wave--back-top" viewBox="0 0 597 90" preserveAspectRatio="none">
      <path d="M0 0 L597 0 L597 30 C420 70 200 10 0 48 Z" fill="var(--wave-light)"/>
      <path d="M0 0 L597 0 L597 18 C420 52 200 0 0 30 Z" fill="var(--wave-blue)"/>
    </svg>
    <div class="speech-bubble speech-bubble--sorry">
      <div class="sorry-title">We Are Sorry</div>
      <div class="sorry-sub">For The Trouble<br>At Your Last Visit</div>
    </div>
    <div class="apology-message">
      <p class="apology-body">Please see attached return of money and we would love to have you back and satisfied.</p>
      <p class="apology-thanks">Thank you again for visiting The Suds Corner.</p>
    </div>
    <svg class="wave wave--back-bottom" viewBox="0 0 597 70" preserveAspectRatio="none">
      <path d="M0 40 C200 10 400 60 597 25 L597 70 L0 70 Z" fill="var(--wave-light)"/>
      <path d="M0 55 C200 30 400 70 597 45 L597 70 L0 70 Z" fill="var(--wave-blue)"/>
    </svg>
    <div class="store-address">418 Elm Ave. Brookfield, SC 29000</div>
  </section>

</body>
</html>
```